依頼詳細
基本的な掲載コンテンツは変更はありません。コンテンツ間の連続性ある個別ページと各コンテンツへのゲートとなるトップページの2ページのデザインを希望いたします。
サイトURL
http://www.kusabe.or.jp/
ページ数
2ページ
希望イメージ
シンプル 複雑
単色 カラフル
暗い 明るい
日常 高級
遊び心 厳粛
未来的 伝統的
女性的 男性的
希望する色
緑・黄・赤
納品ファイル
• イラストレーター形式 (.ai)
• フォトショップ形式 (.psd)
• PNG形式 (.png)
補足説明
CMSはXoopsで構築いたしております。
ご提案いただきました皆様、本当にありがとうございます。

お寄せいただいた提案につきましては、関係者参集の上しっかり検討の上ご連絡差し上げたく存じます。今しばらくお待ちくださいませ。

まずはお礼まで。
■ 選んだ理由

当選案は今回多くの方から頂いた膨大なコンテンツで迷子になるというご指摘に対して、2名だけ下部にサイトマップ型のテキストナビゲーションで配慮された点に大きなポイントがありました。また言葉による説明だけではなく図解をプラスされていた点やデザインの再提出への応対スピード、さらなる修正にもドンドン応じるというメッセージに本気度の高さが見えてしまった点などは不利が有利に転じたポイントでもありました。本当に決定的な差がなく、プラスアルファに成否があったことは選考側にとってはうれしい悲鳴でしたが難航でした。

■ 提案者全員のお礼・コメント

まずは皆様、この度はご提案頂き大変ありがとうございました。どのご提案もよく配慮されており、現状のサイトの問題点を的確にご指摘いただいていました。選考委員が変われば結果も違ったと思うほどどの提案も素晴らしかったです。システムサイドからの視点、ユーザーサイドからの視点、発信者サイドからの視点それぞれの切り口からのご提案はとても興味深くたいへん勉強になりました。今回はご縁がございませんでした方も是非また機会がございましたらご提案くださいますよう、今後ともよろしくお願いいたします。

```html
<!DOCTYPE html>
<html lang="ja">
<head>
<meta charset="utf-8">
<title>草部観光ナビ</title>
<link rel="stylesheet" href="https://fonts.googleapis.com/css2?family=Noto+Sans+JP:wght@400;700&display=swap">
<style>
:root{
  --green:#8cc63f;
  --green-dark:#4f8f1c;
  --green-pale:#eef6de;
  --green-line:#c9e2a0;
  --yellow:#f2c230;
  --red:#d9442b;
  --text:#333;
  --muted:#777;
  --line:#dcdcdc;
  --bg:#fff;
  --photo-a:#9fb98a;
  --photo-b:#c8b79a;
  --photo-c:#8fa9c2;
}
*{box-sizing:border-box;margin:0;padding:0}
html,body{width:1200px;height:3824px;overflow:hidden}
body{font-family:"Noto Sans JP",sans-serif;color:var(--text);background:var(--bg);font-size:12px;line-height:1.5}
a{color:inherit;text-decoration:none}
ul{list-style:none}
.page{width:1160px;margin:0 auto;position:relative}
.site-header{height:100px;display:flex;justify-content:space-between;align-items:flex-start;padding-top:18px}
.brand{display:flex;align-items:center;gap:10px}
.brand-mark{width:26px;height:26px;background:var(--green)}
.brand-name{font-size:26px;font-weight:700;color:var(--green-dark);letter-spacing:2px}
.brand-tag{font-size:11px;color:var(--muted);margin-top:4px}
.util{text-align:right;font-size:11px;color:var(--muted)}
.util-links{display:flex;gap:12px;justify-content:flex-end}
.util-row{display:flex;gap:8px;justify-content:flex-end;margin-top:8px;align-items:center}
.util-btn{background:var(--green);color:#fff;padding:2px 10px;border-radius:2px}
.search{width:170px;height:22px;border:1px solid var(--line)}
.global-nav{height:52px;display:flex;border-bottom:4px solid var(--green)}
.global-nav a{flex:1;display:flex;align-items:center;justify-content:center;font-size:15px;font-weight:700;color:var(--green-dark);border-right:1px solid var(--line)}
.global-nav a:last-child{border-right:0}
.global-nav a.current{background:var(--green);color:#fff}
.hero{display:flex;gap:20px;margin-top:16px;height:236px}
.slide{width:680px}
.slide-img{height:210px;background:linear-gradient(135deg,var(--photo-b),#6e5b46)}
.dots{display:flex;gap:6px;justify-content:center;margin-top:10px}
.dots i{width:8px;height:8px;border-radius:50%;background:var(--line)}
.dots i.on{background:var(--green)}
.finder{width:460px;background:var(--green);padding:12px;color:#fff}
.finder h2{font-size:15px;margin-bottom:10px}
.finder-grid{display:grid;grid-template-columns:repeat(3,1fr);gap:8px}
.finder-grid a{background:#fff;color:var(--green-dark);height:78px;display:flex;flex-direction:column;align-items:center;justify-content:center;font-weight:700;font-size:12px;gap:6px}
.columns{display:flex;gap:20px;margin-top:14px}
.col-main{width:680px}
.col-side{width:460px}
.box{border:1px solid var(--line);margin-bottom:10px;overflow:hidden}
.box-head{display:flex;justify-content:space-between;align-items:center;background:var(--green-pale);border-top:3px solid var(--green);padding:6px 10px}
.box-head h2{font-size:14px;color:var(--green-dark)}
.more{font-size:10px;color:#fff;background:var(--green);padding:1px 8px}
.box-body{padding:10px}
.photo{background:linear-gradient(135deg,var(--photo-a),#5e7f4a)}
.photo.b{background:linear-gradient(135deg,var(--photo-b),#8a6f4e)}
.photo.c{background:linear-gradient(135deg,var(--photo-c),#53708c)}
.item-title{color:var(--green-dark);font-weight:700;font-size:12px}
.item-meta{font-size:10px;color:var(--muted)}
.date{color:var(--red);font-size:10px;margin-right:6px}
.events{display:flex;gap:14px}
.events-feature{width:250px}
.events-feature .photo{height:150px;margin-bottom:8px}
.events-list{flex:1}
.events-list li{padding:8px 0;border-bottom:1px dotted var(--line)}
.banner-grid{display:grid;grid-template-columns:repeat(3,1fr);gap:10px}
.banner{height:104px;display:flex;align-items:flex-end;padding:6px;color:#fff;font-weight:700;font-size:12px}
.banner.plain{background:var(--green-pale);color:var(--green-dark);border:1px solid var(--green-line)}
.wide-banner{height:110px;background:linear-gradient(90deg,#f7e8a6,var(--yellow));display:flex;align-items:center;justify-content:center;font-size:22px;font-weight:700;color:var(--red);margin-bottom:12px}
.report-grid{display:grid;grid-template-columns:1fr 1fr;gap:14px 20px}
.report{display:flex;gap:10px}
.report .photo{width:120px;height:90px;flex:none}
.report p{font-size:11px;color:var(--muted)}
.thumb-grid{display:grid;grid-template-columns:repeat(4,1fr);gap:10px}
.thumb .photo{height:82px;margin-bottom:4px}
.thumb p{font-size:11px}
.fan{display:flex;gap:14px}
.fan-col{flex:1}
.fan-logo{display:flex;align-items:center;gap:8px;font-weight:700;color:var(--green-dark);font-size:16px;padding:8px 0;border-bottom:2px solid var(--green);margin-bottom:8px}
.fan-logo i{width:14px;height:14px;background:var(--green);display:block}
.fan-col li{padding:6px 0;border-bottom:1px dotted var(--line)}
.icon-list li{display:flex;gap:8px;align-items:center}
.icon-list li b{width:18px;height:18px;background:var(--green);flex:none;display:block;border-radius:2px}
.tabs{display:flex}
.tabs span{flex:1;text-align:center;padding:6px;font-weight:700;background:var(--green-pale);color:var(--green-dark);border-top:3px solid var(--green-line)}
.tabs span.on{background:#fff;border-top-color:var(--green)}
.news li{padding:6px 0;border-bottom:1px dotted var(--line);font-size:11px}
.side-banners{display:grid;grid-template-columns:1fr 1fr;gap:8px;margin-bottom:10px}
.side-banners div{height:50px;background:var(--green-pale);border:1px solid var(--green-line);display:flex;align-items:center;justify-content:center;font-weight:700;color:var(--green-dark)}
.side-banners div.wide{grid-column:span 2;height:50px;background:var(--yellow);color:#fff}
.blog-grid{display:grid;grid-template-columns:1fr 1fr;gap:10px}
.blog-grid .photo{height:70px;margin-bottom:4px}
.rank li{display:flex;gap:8px;align-items:center;padding:5px 0;border-bottom:1px dotted var(--line);font-size:11px}
.rank .num{width:18px;height:18px;background:var(--yellow);color:#fff;font-size:10px;display:flex;align-items:center;justify-content:center;flex:none}
.rank .photo{width:50px;height:36px;flex:none}
.week li{padding:5px 0;border-bottom:1px dotted var(--line);font-size:11px}
.week h3{font-size:11px;color:var(--green-dark);background:var(--green-pale);padding:2px 6px;margin-top:6px}
.field{height:24px;border:1px solid var(--line);margin:6px 0}
.btn{display:inline-block;background:var(--green);color:#fff;padding:3px 16px}
.useful{margin-top:6px;border-top:3px solid var(--green);padding:10px}
.useful h2{font-size:14px;color:var(--green-dark);margin-bottom:8px}
.useful p{font-size:11px;color:var(--muted)}
.sitemap{background:var(--green-pale);margin-top:60px;padding:24px 0;height:330px}
.sitemap-inner{width:1160px;margin:0 auto;display:grid;grid-template-columns:repeat(6,1fr);gap:16px}
.sitemap h3{font-size:12px;color:var(--green-dark);border-bottom:1px solid var(--green-line);margin-bottom:6px}
.sitemap li{font-size:11px;color:var(--muted);padding:2px 0}
.foot-links{text-align:center;font-size:11px;color:var(--muted);padding:14px 0;border-bottom:4px solid var(--green)}
.site-footer{width:1160px;margin:30px auto 0;display:flex;justify-content:space-between;font-size:11px;color:var(--muted)}
.site-footer .brand-name{font-size:20px}
.copy{text-align:center;font-size:10px;color:var(--muted);margin-top:40px}
</style>
</head>
<body>
<div class="page">
  <header class="site-header">
    <div>
      <div class="brand"><span class="brand-mark"></span><span class="brand-name">草部観光ナビ</span></div>
      <div class="brand-tag">Kusabe Tourism ／ 草部の旅と暮らしの情報サイト</div>
    </div>
    <div class="util">
      <ul class="util-links"><li>このサイトについて</li><li>サイトマップ</li><li>お問い合わせ</li><li>English</li></ul>
      <div class="util-row"><span>文字サイズ</span><span class="util-btn">小</span><span class="util-btn">中</span><span class="util-btn">大</span><span class="search"></span><span class="util-btn">検索</span></div>
    </div>
  </header>
  <nav class="global-nav">
    <a href="#">イベント</a><a href="#" class="current">観光ナビ</a><a href="#">くさべグルメナビ</a><a href="#">ライフナビ</a><a href="#">ブログ</a><a href="#">リンク</a>
  </nav>

  <section class="hero">
    <div class="slide">
      <div class="slide-img" role="img" aria-label="名物のそばと茶の並ぶ食卓の写真"></div>
      <div class="dots"><i class="on"></i><i></i><i></i><i></i><i></i></div>
    </div>
    <div class="finder">
      <h2>草部を見る・体験・探せる</h2>
      <div class="finder-grid">
        <a href="#"><svg width="26" height="26" viewBox="0 0 26 26"><circle cx="13" cy="11" r="6" fill="none" stroke="#8cc63f" stroke-width="3"/><path d="M13 17v7" stroke="#8cc63f" stroke-width="3"/></svg>観光スポット</a>
        <a href="#"><svg width="26" height="26" viewBox="0 0 26 26"><rect x="3" y="6" width="20" height="16" fill="none" stroke="#8cc63f" stroke-width="3"/></svg>宿泊施設</a>
        <a href="#"><svg width="26" height="26" viewBox="0 0 26 26"><path d="M5 4v18M9 4v18M7 4v8" stroke="#8cc63f" stroke-width="3"/><path d="M18 4v18" stroke="#8cc63f" stroke-width="3"/></svg>グルメ</a>
        <a href="#"><svg width="26" height="26" viewBox="0 0 26 26"><path d="M13 3a7 7 0 0 1 7 7c0 6-7 13-7 13S6 16 6 10a7 7 0 0 1 7-7z" fill="#8cc63f"/></svg>地図から探す</a>
        <a href="#"><svg width="26" height="26" viewBox="0 0 26 26"><path d="M4 13l6 6L22 7" fill="none" stroke="#8cc63f" stroke-width="3"/></svg>体験・遊ぶ</a>
        <a href="#"><svg width="26" height="26" viewBox="0 0 26 26"><path d="M6 13h14M14 7l6 6-6 6" fill="none" stroke="#8cc63f" stroke-width="3"/></svg>モデルコース</a>
      </div>
    </div>
  </section>

  <div class="columns">
    <main class="col-main">
      <section class="box" style="height:370px">
        <div class="box-head"><h2>イベント情報</h2><span class="more">一覧へ</span></div>
        <div class="box-body events">
          <div class="events-feature">
            <div class="photo" role="img" aria-label="秋の祭りに集う人々の写真"></div>
            <p class="item-title">秋の収穫まつり 開催のお知らせ</p>
            <p class="item-meta">2014年10月12日 会場：草部中央公園</p>
          </div>
          <ul class="events-list">
            <li><span class="date">10/04</span><span class="item-title">草部ゲームパークでイベント開催</span><p class="item-meta">家族で楽しめる体験が盛りだくさん</p></li>
            <li><span class="date">10/11</span><span class="item-title">高原ウォーキング大会 参加者募集</span><p class="item-meta">紅葉の山道を歩くコースです</p></li>
            <li><span class="date">10/18</span><span class="item-title">そば打ち体験教室のご案内</span><p class="item-meta">地元の名人が丁寧に教えます</p></li>
            <li><span class="date">10/25</span><span class="item-title">朝市フェスタ 出店者決定</span><p class="item-meta">旬の野菜と加工品が並びます</p></li>
            <li><span class="date">11/01</span><span class="item-title">温泉街ライトアップ開始</span><p class="item-meta">夜の街並みを灯りが彩ります</p></li>
          </ul>
        </div>
      </section>

      <section class="box" style="height:540px">
        <div class="box-head"><h2>気になるコンテンツ</h2></div>
        <div class="box-body banner-grid">
          <div class="banner photo" role="img" aria-label="ファンクラブ案内のバナー写真">草部ファンクラブ</div>
          <div class="banner plain">雪の情報 2014</div>
          <div class="banner plain">フォトコンテスト</div>
          <div class="banner photo b" role="img" aria-label="棚田の風景写真">スタンプラリー</div>
          <div class="banner photo c" role="img" aria-label="山並みの風景写真">草部の旅 特集</div>
          <div class="banner plain">草部いなか暮らし</div>
          <div class="banner photo" role="img" aria-label="草原の写真">くさべ まなび</div>
          <div class="banner photo b" role="img" aria-label="田園風景の写真">里山伝説めぐり</div>
          <div class="banner plain">草部高原ジオパーク</div>
          <div class="banner photo c" role="img" aria-label="山の写真">観光パンフレット</div>
          <div class="banner plain">草部の旅 季刊誌</div>
          <div class="banner photo" role="img" aria-label="森の写真">ロケ地ガイド</div>
        </div>
      </section>

      <section class="box" style="height:760px">
        <div class="box-head"><h2>ふるさと特派員</h2><span class="more">一覧へ</span></div>
        <div class="box-body">
          <div class="wide-banner">草部を巡るベスト観光ルート</div>
          <div class="report-grid">
            <div class="report"><div class="photo" role="img" aria-label="紅葉の山の写真"></div><div><p class="item-title">紅葉の山道を歩いてきました</p><p>色づく木々の中を散策し季節の移ろいを感じました。</p></div></div>
            <div class="report"><div class="photo b" role="img" aria-label="古い町並みの写真"></div><div><p class="item-title">城下町の路地をめぐる</p><p>昔ながらの町家と小さな店を訪ねました。</p></div></div>
            <div class="report"><div class="photo c" role="img" aria-label="川の写真"></div><div><p class="item-title">清流沿いのサイクリング</p><p>澄んだ川に沿って心地よく走れるコースです。</p></div></div>
            <div class="report"><div class="photo" role="img" aria-label="田んぼの写真"></div><div><p class="item-title">稲刈り体験に参加して</p><p>地域の方と一緒に実りの秋を味わいました。</p></div></div>
            <div class="report"><div class="photo b" role="img" aria-label="郷土料理の写真"></div><div><p class="item-title">郷土料理の店を訪問</p><p>素朴でやさしい味わいに心が和みました。</p></div></div>
            <div class="report"><div class="photo c" role="img" aria-label="海岸の写真"></div><div><p class="item-title">海岸の夕景を撮影</p><p>夕日に染まる岩場がとても印象的でした。</p></div></div>
            <div class="report"><div class="photo" role="img" aria-label="神社の写真"></div><div><p class="item-title">山里の神社で秋祭り</p><p>太鼓の音が谷に響き渡っていました。</p></div></div>
            <div class="report"><div class="photo b" role="img" aria-label="温泉街の写真"></div><div><p class="item-title">温泉街のそぞろ歩き</p><p>外湯めぐりで身も心も温まりました。</p></div></div>
          </div>
        </div>
      </section>

      <section class="box" style="height:330px">
        <div class="box-head"><h2>ヘッドライン</h2><span class="more">一覧へ</span></div>
        <div class="box-body thumb-grid">
          <div class="thumb"><div class="photo c" role="img" aria-label="夜景の写真"></div><p>夜の灯りイベント</p></div>
          <div class="thumb"><div class="photo" role="img" aria-label="山の写真"></div><p>高原の秋景色</p></div>
          <div class="thumb"><div class="photo b" role="img" aria-label="町の写真"></div><p>町歩きマップ公開</p></div>
          <div class="thumb"><div class="photo c" role="img" aria-label="川の写真"></div><p>川下り体験</p></div>
          <div class="thumb"><div class="photo b" role="img" aria-label="祭りの写真"></div><p>秋祭りの記録</p></div>
          <div class="thumb"><div class="photo" role="img" aria-label="田園の写真"></div><p>里山の暮らし</p></div>
          <div class="thumb"><div class="photo c" role="img" aria-label="海の写真"></div><p>海辺の朝</p></div>
          <div class="thumb"><div class="photo b" role="img" aria-label="料理の写真"></div><p>冬の味覚特集</p></div>
        </div>
      </section>

      <section class="box" style="height:340px">
        <div class="box-head"><h2>草部ファンクラブ</h2><span class="more">会員登録</span></div>
        <div class="box-body fan">
          <div class="fan-col">
            <div class="fan-logo"><i></i>Kusabe Fan Club</div>
            <ul>
              <li><span class="date">10/01</span>会員限定 秋の特典のご案内</li>
              <li><span class="date">09/20</span>会報誌 秋号を発行しました</li>
              <li><span class="date">09/05</span>交流会 参加者募集中</li>
              <li><span class="date">08/28</span>新規会員キャンペーン実施</li>
            </ul>
          </div>
          <div class="fan-col">
            <div class="fan-logo" style="font-size:14px">草部の旅に お役立ち情報</div>
            <ul class="icon-list">
              <li><b></b>アクセス・交通案内</li>
              <li><b></b>観光案内所のご紹介</li>
              <li><b></b>パンフレット請求</li>
              <li><b></b>よくあるご質問</li>
            </ul>
          </div>
        </div>
      </section>
    </main>

    <aside class="col-side">
      <section class="box" style="height:240px">
        <div class="tabs"><span class="on">トピックス</span><span>観光特派</span></div>
        <div class="box-body"><ul class="news">
          <li><span class="date">10/03</span>秋の観光キャンペーン始まります</li>
          <li><span class="date">10/01</span>紅葉の見ごろ情報を更新しました</li>
          <li><span class="date">09/29</span>臨時バスの運行についてのお知らせ</li>
          <li><span class="date">09/25</span>新しい観光マップを配布しています</li>
          <li><span class="date">09/20</span>草部の特産品フェア開催のお知らせ</li>
          <li><span class="date">09/15</span>サイトをリニューアルしました</li>
        </ul></div>
      </section>
      <div class="side-banners">
        <div class="wide">草部でいなか暮らし</div>
        <div>くさべ体験ナビ</div><div>くさべ 山の会</div>
      </div>
      <section class="box" style="height:330px">
        <div class="box-head"><h2>くさべのいなかブログ</h2><span class="more">一覧へ</span></div>
        <div class="box-body blog-grid">
          <div><div class="photo" role="img" aria-label="畑の写真"></div><p class="item-title">畑の収穫日記</p><p class="item-meta">10/02 更新</p></div>
          <div><div class="photo b" role="img" aria-label="古民家の写真"></div><p class="item-title">古民家の手入れ</p><p class="item-meta">09/30 更新</p></div>
          <div><div class="photo c" role="img" aria-label="川辺の写真"></div><p class="item-title">川辺の散歩道</p><p class="item-meta">09/27 更新</p></div>
          <div><div class="photo" role="img" aria-label="山の写真"></div><p class="item-title">山の朝霧</p><p class="item-meta">09/24 更新</p></div>
        </div>
      </section>
      <section class="box" style="height:250px">
        <div class="box-head"><h2>アクセスランキング</h2></div>
        <div class="box-body"><ul class="rank">
          <li><span class="num">1</span><span class="photo" role="img" aria-label="観光地の写真"></span>高原の紅葉スポット</li>
          <li><span class="num">2</span><span class="photo b" role="img" aria-label="温泉の写真"></span>温泉街の楽しみ方</li>
          <li><span class="num">3</span><span class="photo c" role="img" aria-label="海の写真"></span>海岸ドライブコース</li>
          <li><span class="num">4</span><span class="photo" role="img" aria-label="城跡の写真"></span>城跡と雲海の眺め</li>
        </ul></div>
      </section>
      <section class="box week" style="height:700px">
        <div class="box-head"><h2>1週間のイベント</h2><span class="more">一覧へ</span></div>
        <div class="box-body">
          <h3>2014年10月4日（土）</h3>
          <ul><li>秋の収穫まつり（中央公園）</li><li>里山ウォーク（北部地区）</li><li>地元野菜の朝市</li><li>竹細工体験教室</li><li>星空観察会（高原ロッジ）</li></ul>
          <h3>2014年10月5日（日）</h3>
          <ul><li>そば打ち体験教室</li><li>川下りカヌー体験</li><li>郷土芸能の発表会</li><li>写真展「草部の四季」</li></ul>
          <h3>2014年10月6日（月）</h3>
          <ul><li>温泉街ライトアップ</li><li>地元料理の講習会</li></ul>
          <h3>2014年10月7日（火）</h3>
          <ul><li>ミュージアム特別展示</li><li>陶芸体験教室</li><li>里山の自然観察</li></ul>
          <h3>2014年10月8日（水）</h3>
          <ul><li>歴史講座「城下町の成り立ち」</li><li>親子クラフト教室</li></ul>
        </div>
      </section>
      <section class="box" style="height:240px">
        <div class="box-head"><h2>美術館開催イベント</h2></div>
        <div class="box-body"><ul class="news">
          <li><span class="date">10/10</span>秋の企画展「山と水の絵画」</li>
          <li><span class="date">10/18</span>ギャラリートークを開催します</li>
          <li><span class="date">11/01</span>子ども向けワークショップ</li>
          <li><span class="date">11/15</span>収蔵品の特別公開</li>
        </ul></div>
      </section>
      <section class="box" style="height:200px">
        <div class="box-head"><h2>公式アカウント</h2></div>
        <div class="box-body"><ul class="news">
          <li>高原の紅葉が見ごろを迎えています。</li>
          <li>今週末は朝市が開かれます。</li>
          <li>新しい観光マップができました。</li>
        </ul></div>
      </section>
      <section class="box" style="height:180px">
        <div class="box-head"><h2>メルマガ登録・解除</h2></div>
        <div class="box-body">
          <p>最新の観光情報をお届けします。</p>
          <div class="field"></div>
          <span class="btn">登録</span> <span class="btn">解除</span>
        </div>
      </section>
    </aside>
  </div>

  <section class="useful">
    <h2>お役立ちリンク</h2>
    <p>交通案内 ｜ 気象情報 ｜ 道路情報 ｜ 観光協会 ｜ 市町村 ｜ 宿泊予約 ｜ 体験予約 ｜ 物産館 ｜ 観光案内所 ｜ 文化施設 ｜ 自然公園 ｜ 地域情報</p>
  </section>
</div>

<footer>
  <div class="sitemap">
    <div class="sitemap-inner">
      <div><h3>イベント</h3><ul><li>イベント一覧</li><li>1週間のイベント</li><li>季節の行事</li><li>美術館イベント</li></ul></div>
      <div><h3>観光ナビ</h3><ul><li>観光スポット</li><li>宿泊施設</li><li>モデルコース</li><li>地図から探す</li><li>体験・遊ぶ</li></ul></div>
      <div><h3>くさべグルメナビ</h3><ul><li>郷土料理</li><li>特産品</li><li>食事処</li><li>カフェ</li></ul></div>
      <div><h3>ライフナビ</h3><ul><li>いなか暮らし</li><li>移住案内</li><li>まなび</li><li>くらしの情報</li></ul></div>
      <div><h3>ブログ</h3><ul><li>いなかブログ</li><li>ふるさと特派員</li><li>ヘッドライン</li></ul></div>
      <div><h3>リンク</h3><ul><li>お役立ちリンク</li><li>関連団体</li><li>ファンクラブ</li><li>メルマガ</li></ul></div>
    </div>
  </div>
  <p class="foot-links">このサイトについて ｜ 個人情報の取扱い ｜ リンクについて ｜ サイトマップ ｜ お問い合わせ</p>
  <div class="site-footer">
    <div>
      <div class="brand"><span class="brand-mark"></span><span class="brand-name">草部観光ナビ</span></div>
      <p style="margin-top:8px">草部観光協議会 ／ 〒600-0000 草部市中央町1-2-3</p>
      <p>http://www.kusabe.or.jp/</p>
    </div>
    <div style="text-align:right">
      <p>草部広域観光事務局</p>
      <p>受付 9:00〜17:00（土日祝休）</p>
    </div>
  </div>
  <p class="copy">Copyright © 2014 Kusabe Tourism All Rights Reserved.</p>
</footer>
</body>
</html>
```